Aviation Law Firm Needs Envelope Design

The envelope design must be EYE CATCHING and sexy, yet very professional. The information in the return address should be in the upper left hand corner and read:
The Marrow Law Firm
P.O. Box 9187
Harlow Springs, Westmark 33912

The word: "ADVERTISEMENT" must appear on the front of the envelope in some fashion.

The colors should compliment the letterhead image (attached). However, I would like for the envelope to remain white or light colored in the upper right hand corner so that the post office can read any stamps, etc.

Target Market(s)

Pilots; Legal Clients

Industry/Entity Type

Law Firm

Font styles to use
Serif
Sans Serif

Colors
191919
fbee3e
ffffff

Requirements
Must have
• Must capture the use of the entire envelope, BUT leave space for receiver's address and post office stamps, etc.

```html
<!DOCTYPE html>
<html lang="en">
<head>
<meta charset="utf-8">
<title>The Marrow Law Firm — Envelope</title>
<link href="https://fonts.googleapis.com/css2?family=Arimo:wght@700&family=Open+Sans:wght@700&family=Roboto:wght@400&display=swap" rel="stylesheet">
<style>
  :root {
    --ink: #191919;
    --signal: #fbee3e;
    --paper: #ffffff;
    --backdrop: #ececec;
    --signal-faint: #f8f3cf;
  }
  * { box-sizing: border-box; margin: 0; padding: 0; }
  html, body { width: 1200px; height: 800px; overflow: hidden; background: var(--backdrop); }
  .canvas { position: relative; width: 1200px; height: 800px; }

  .envelope {
    position: absolute;
    left: 170px;
    width: 860px;
    height: 360px;
    background: var(--paper);
    overflow: hidden;
    box-shadow: 0 2px 6px rgba(0,0,0,0.12);
  }
  .envelope--front { top: 24px; }
  .envelope--back { top: 410px; }

  /* Front */
  .return-address {
    position: absolute;
    left: 28px;
    top: 16px;
    font-family: "Arimo", Arial, sans-serif;
    font-weight: 700;
    font-size: 15px;
    letter-spacing: 2px;
    line-height: 22px;
    color: var(--ink);
    font-style: normal;
  }
  .firm-mark {
    position: absolute;
    left: 40px;
    top: 132px;
    display: flex;
    align-items: center;
    gap: 10px;
    font-family: "Arimo", Arial, sans-serif;
    font-weight: 700;
    font-size: 14px;
    letter-spacing: 1px;
    color: var(--ink);
  }
  .firm-mark__dot { width: 28px; height: 28px; border-radius: 50%; background: var(--signal); }
  .accent-frame { position: absolute; inset: 0; }
  .bar-black--front { position: absolute; left: 0; top: 262px; width: 272px; height: 36px; background: var(--ink); }
  .band-yellow--front { position: absolute; left: 280px; top: 284px; right: 60px; bottom: 0; background: var(--signal); }
  .advertisement {
    position: absolute;
    right: 104px;
    bottom: 12px;
    font-family: "Open Sans", Arial, sans-serif;
    font-weight: 700;
    font-size: 25px;
    letter-spacing: 5px;
    color: var(--ink);
  }

  /* Back */
  .bar-black--back { position: absolute; left: 0; top: 0; width: 232px; height: 50px; background: var(--ink); }
  .band-yellow--back {
    position: absolute; left: 238px; top: 50px; right: 0; height: 62px;
    background: var(--signal);
    display: flex; align-items: center; padding-left: 12px;
    font-family: "Roboto", Arial, sans-serif; font-size: 25px; letter-spacing: 2px; color: var(--ink);
  }
  .flap-name {
    position: absolute; left: 0; right: 0; top: 200px; text-align: center;
    font-family: "Roboto", Arial, sans-serif; font-size: 40px; letter-spacing: 2px;
    color: var(--signal-faint);
  }
</style>
</head>
<body>
<main class="canvas">
  <section class="envelope envelope--front">
    <address class="return-address">
      The Marrow Law Firm<br>
      P.O. Box 9187<br>
      Harlow Springs, Westmark 33912
    </address>
    <div class="firm-mark"><span class="firm-mark__dot"></span>The Marrow Law Firm</div>
    <div class="bar-black--front"></div>
    <div class="band-yellow--front"></div>
    <svg class="accent-frame" width="860" height="360" viewBox="0 0 860 360">
      <path d="M800 0 L860 0 L860 360 L770 360 Q792 320 794 240 Z" fill="var(--signal)"/>
      <path d="M800 0 L794 240 Q792 320 770 360" fill="none" stroke="var(--ink)" stroke-width="3"/>
    </svg>
    <div class="advertisement">ADVERTISEMENT</div>
  </section>

  <section class="envelope envelope--back">
    <div class="bar-black--back"></div>
    <div class="band-yellow--back">The Marrow Law Firm</div>
    <div class="flap-name">The Marrow Law Firm</div>
  </section>
</main>
</body>
</html>
```